Company Profile

Redesign of Business Profile for print in A4 format. The design pages should complete a booklet. Kindly use Pictures as well as projects from our website @molekwaestates.co.za

Target Market(s)

Business, Construction

```html
<!DOCTYPE html>
<html lang="en">
<head>
<meta charset="utf-8">
<title>Molekwa Estates — Company Profile Cover</title>
<link rel="stylesheet" href="https://fonts.googleapis.com/css2?family=Open+Sans:wght@300;400&family=Oswald:wght@500&display=swap">
<style>
  :root {
    --charcoal: #353133;
    --brick: #7e2b1f;
    --brick-deep: #6e2418;
    --white: #ffffff;
    --ink: #111011;
    --mist: #d2d0d0;
    --tag-grey: #a9a7a8;
    --photo-aerial: #8c7a63;
    --photo-interior: #a9a9a6;
    --photo-housing: #a8633e;
  }
  * { margin: 0; padding: 0; box-sizing: border-box; }
  html, body { width: 848px; height: 1200px; overflow: hidden; background: var(--charcoal); }
  .cover {
    position: relative;
    width: 848px;
    height: 1200px;
    background: var(--charcoal);
    overflow: hidden;
    font-family: "Open Sans", Arial, sans-serif;
  }
  .swoosh { position: absolute; left: 0; width: 848px; display: block; }
  .swoosh--top { top: 0; height: 240px; }
  .swoosh--bottom { bottom: 0; height: 360px; }
  .web-address {
    position: absolute;
    top: 15px;
    right: 28px;
    font-size: 13.5px;
    font-weight: 400;
    color: var(--tag-grey);
    letter-spacing: 0.2px;
  }
  .tagline {
    position: absolute;
    left: 121px;
    top: 136px;
    font-size: 32px;
    line-height: 1;
    font-weight: 300;
    color: var(--tag-grey);
    transform: rotate(-23.5deg);
    transform-origin: 0 28px;
    white-space: nowrap;
  }
  .project-gallery {
    position: absolute;
    left: 84px;
    top: 363px;
    width: 681px;
    height: 286px;
    border-radius: 22px;
    overflow: hidden;
    display: grid;
    grid-template-columns: 434px 247px;
    grid-template-rows: 147px 139px;
    box-shadow: 0 6px 18px rgba(0,0,0,0.45);
  }
  .project-photo--aerial {
    grid-row: 1 / 3;
    background: linear-gradient(160deg, #6f7a5a 0%, var(--photo-aerial) 45%, #9b9a94 100%);
  }
  .project-photo--interior {
    background: linear-gradient(180deg, #cfd1cf 0%, var(--photo-interior) 60%, #8f7a66 100%);
  }
  .project-photo--housing {
    background: linear-gradient(180deg, #5f6a45 0%, #9a6a44 40%, var(--photo-housing) 100%);
  }
  .mission {
    position: absolute;
    left: 0;
    top: 708px;
    width: 848px;
    text-align: center;
    font-size: 15.3px;
    line-height: 20.4px;
    font-weight: 400;
    color: var(--mist);
    text-transform: uppercase;
    letter-spacing: -0.1px;
  }
  .page-tab {
    position: absolute;
    left: -22px;
    top: 1145px;
    width: 111px;
    height: 43px;
    border-radius: 22px;
    background: var(--white);
  }
  .brand-name {
    position: absolute;
    right: 17px;
    top: 1094px;
    width: 230px;
    text-align: right;
    font-family: "Oswald", "Arial Narrow", sans-serif;
    font-weight: 500;
    color: var(--white);
  }
  .brand-name__main { display: block; font-size: 44px; line-height: 48px; letter-spacing: 0.5px; }
  .brand-name__sub { display: block; font-size: 17px; line-height: 24px; letter-spacing: 9.5px; margin-right: -9px; }
</style>
</head>
<body>
<main class="cover">
  <svg class="swoosh swoosh--top" viewBox="0 0 848 240" preserveAspectRatio="none" aria-hidden="true">
    <path fill="var(--brick)" d="M0,60 C100,45 220,20 290,0 L350,0 C250,60 130,115 0,138 Z"/>
    <path fill="var(--white)" d="M0,153 C130,125 250,65 360,0 L503,0 C380,110 200,185 0,217 Z"/>
    <path fill="var(--brick)" d="M121,216 C330,165 520,85 627,0 L540,0 C440,90 300,160 121,216 Z"/>
  </svg>

  <p class="web-address">www.molekwaestates.co.za</p>
  <p class="tagline">achieving distinction</p>

  <section class="project-gallery">
    <div class="project-photo--aerial" role="img" aria-label="Aerial photograph of a completed residential complex with pool, tennis court and roads"></div>
    <div class="project-photo--interior" role="img" aria-label="Photograph of a modern apartment living room with leather sofa and glass partition"></div>
    <div class="project-photo--housing" role="img" aria-label="Photograph of rows of newly built low-cost houses on red earth"></div>
  </section>

  <p class="mission">
    Committed to growing the economy by<br>
    contributing to infrastructure development through the provision of<br>
    world class services in roads &amp; civils, buildings, water &amp; sanitation,<br>
    structures &amp; property development in<br>
    South Africa
  </p>

  <svg class="swoosh swoosh--bottom" viewBox="0 0 848 360" preserveAspectRatio="none" aria-hidden="true">
    <path fill="var(--brick)" d="M0,273 C320,250 660,140 848,30 L848,360 L0,360 Z"/>
    <path fill="var(--white)" d="M150,360 C460,320 720,200 848,85 L848,110 C730,230 500,345 260,360 Z"/>
    <path fill="var(--ink)" d="M260,360 C500,345 730,230 848,110 L848,120 C740,240 520,352 320,360 Z"/>
    <path fill="var(--brick-deep)" d="M320,360 C520,352 740,240 848,120 L848,360 Z"/>
  </svg>

  <div class="page-tab"></div>

  <p class="brand-name">
    <span class="brand-name__main">MOLEKWA</span>
    <span class="brand-name__sub">ESTATES</span>
  </p>
</main>
</body>
</html>
```